Luxury Brand Real Estate For Sale sign

**Update** I've added some examples from the internet of other signs that have a look similar to what I would like to see. I do not want my personal name in the sign. And the word FOR SALE Does not need to be so large - it can be more subtle.
I want to create a Real Estate for sale sign for my company that will be used for luxury/higher end real estate listings. I’m sharing my business card as well as a logo with new teal color to show what we're moving towards: we’re using Teal, white, black and gold.
Hoping the sign is simple, sophisticated and eye catching.
The sign should be 24" wide by 30" tall including the company name: Harbor Crest Realty Group and our logo, office phone number 727-555-0148 and website www.hcrgproperty.example the words "For Sale"
Optional to add this e-mail address info@hcrgproperty.example to the sign
Luxury home buyers
Real Estate

```html
<!DOCTYPE html>
<html lang="en">
<head>
<meta charset="utf-8">
<title>Harbor Crest Realty Group – For Sale Sign</title>
<link href="https://fonts.googleapis.com/css2?family=Josefin+Sans:wght@400&family=Open+Sans:wght@600;700;800&family=Arimo:wght@700&display=swap" rel="stylesheet">
<style>
  :root {
    --white: #ffffff;
    --teal: #028080;
    --gold: #b6a05d;
    --brand-gold: #b38b30;
    --plum: #5a3c46;
  }
  html, body {
    margin: 0;
    padding: 0;
    overflow: hidden;
    background: var(--white);
  }
  .sign {
    position: relative;
    width: 960px;
    height: 1200px;
    overflow: hidden;
    background: var(--white);
  }
  .brand-band {
    position: absolute;
    left: 0; top: 0;
    width: 960px; height: 388px;
    background: var(--white);
  }
  .brand-square {
    position: absolute;
    left: 190px; top: 184px;
    width: 80px; height: 80px;
    box-sizing: border-box;
    border: 4px solid var(--brand-gold);
  }
  .brand-divider {
    position: absolute;
    left: 349px; top: 114px;
    width: 4px; height: 227px;
    background: var(--plum);
  }
  .brand-name {
    position: absolute;
    left: 385px; top: 190px;
    margin: 0;
    font-family: "Josefin Sans", sans-serif;
    font-weight: 400;
    font-size: 30px;
    line-height: 40px;
    letter-spacing: 2px;
    color: var(--brand-gold);
    text-transform: uppercase;
  }
  .listing-band {
    position: absolute;
    left: 0; top: 388px;
    width: 960px; height: 682px;
    background: var(--teal);
  }
  .sale-panel {
    position: absolute;
    left: 128px; top: 78px;
    width: 704px; height: 457px;
    background: var(--gold);
  }
  .sale-frame {
    position: absolute;
    left: 20px; top: 25px;
    width: 664px; height: 407px;
    box-sizing: border-box;
    border: 5px solid var(--white);
  }
  .sale-for {
    position: absolute;
    left: 0; top: 0;
    width: 704px;
    margin: 0;
    text-align: center;
    font-family: "Open Sans", sans-serif;
    font-weight: 600;
    font-size: 114px;
    line-height: 1;
    color: var(--white);
    top: 25px;
  }
  .sale-word {
    position: absolute;
    left: 0;
    top: 96px;
    width: 704px;
    margin: 0;
    text-align: center;
    font-family: "Open Sans", sans-serif;
    font-weight: 800;
    font-size: 214px;
    line-height: 1;
    letter-spacing: -6px;
    color: var(--white);
  }
  .phone-box {
    position: absolute;
    left: 43px; top: 315px;
    width: 618px; height: 89px;
    background: var(--white);
    display: flex;
    align-items: center;
    justify-content: center;
    font-family: "Arimo", sans-serif;
    font-weight: 700;
    font-size: 66px;
    color: var(--gold);
    letter-spacing: -1px;
  }
  .web-band {
    position: absolute;
    left: 0; top: 1070px;
    width: 960px; height: 130px;
    background: var(--gold);
    display: flex;
    align-items: center;
    justify-content: center;
    font-family: "Arimo", sans-serif;
    font-weight: 700;
    font-size: 52px;
    color: var(--white);
  }
</style>
</head>
<body>
  <div class="sign">
    <header class="brand-band">
      <div class="brand-square"></div>
      <div class="brand-divider"></div>
      <p class="brand-name">Harbor Crest<br>Realty Group</p>
    </header>

    <section class="listing-band">
      <div class="sale-panel">
        <div class="sale-frame"></div>
        <p class="sale-for">FOR</p>
        <p class="sale-word">SALE</p>
        <div class="phone-box">727-555-0148</div>
      </div>
    </section>

    <footer class="web-band">www.hcrgproperty.example</footer>
  </div>
</body>
</html>
```